Zielgruppe
Ich bin Selfpublisher und habe eine Lust Wunschzettel als Buch kreiert. Die Zielgruppe sind meist junge Erwachsene, aber auch welche mittleren alters.
Aufgabenstellung
Titel des Buches: Der dicke LUST WUNSCHZETTEL
Untertitel: 150 Orte +10 eigene Orte für mehr Nervenkitzel und Erlebnisse
Der Anfang vom Titel 'Die große' kann ruhig sehr klein abgebildet werden.
Das Wort 'SEX' im Titel soll am größten auf dem Cover sein und auch bei kleinster Darstellung gut sichtbar und sehr prägnant sein.
Der Teil vom Untertitel '+10 eigene Orte für mehr Nervenkitzel und Erlebnisse' kann ruhig getrennt von den '150 Orten' stehen.
In dem Buch sind 150 Orte plus jeweils Felder zum Ankreuzen und beschreiben vorhanden, wie der Sex dort war.
Farben: Die Hauptfarbe soll ins rote gehen.
Auf keinen Fall darf dieses Rot #EE3A43 benutzt werden, da dies die Farbe eines Mitbewerbers ist.
Hier zwei Beispiele welche Farben benutzt werden können: #FF4D8D, #FF6686. Natürlich sind auch andere und ähnliche Farben in Ordnung. Dies diente nur zur Orientierung, wie weit das Rot verändert werden muss.
Es sollen keine echten Fotos verwendet werden. Außerdem sollen keine Menschen, oder Illustrationen von Menschen abgebildet werden.
Ich habe eine Datei hochgeladen, worin sich mehrere Illustrationen befinden. Die können in der Farbe und vom Aussehen verändert werden. Das benutzen der Illustrationen ist absolut kein muss! Ich lasse mich gerne von anderen Designs überraschen.
Mit den Illustrationen könnte man zum Beispiel sowas wie auf dem Cover der 'Onkel Tourenheft' abgebildet machen. Bild ist im Anhang. Hierfür müssen die Illustrationen (Sex Icons) mit passenden Farben versehen werden. Es sollte nicht zu Bunt werden, also hier 3-4 Farben aussuchen.
Außerdem eventuell ein Schrift Effekt wie bei dem Titel der 'Garden Quest' auch im Anhang zu finden. Natürlich gehen auch andere passende Effekte. Hier kenne ich mich nicht aus, was so möglich ist.
Es sollte allgemein nicht zu langweilig sein. Etwas Dynamik und Effekte sind gut. Wie bei den bereits genannten Beispiel Covern.

```html
<!DOCTYPE html>
<html lang="de">
<head>
<meta charset="utf-8">
<title>Der dicke LUST WUNSCHZETTEL – Buchcover</title>
<link href="https://fonts.googleapis.com/css2?family=Titan+One&family=Bebas+Neue&display=swap" rel="stylesheet">
<style>
  :root {
    --stage: #F1CCDD;
    --cover: #FF4A8D;
    --cover-light: #FF86B4;
    --heart-line: #FF7EAD;
    --title-shadow: #D92B6E;
    --icon-fill: #FF8DB9;
    --white: #FFFFFF;
    --badge: #FFC20E;
    --badge-text: #2B1A1F;
  }
  * { margin: 0; padding: 0; box-sizing: border-box; }
  html, body {
    width: 1200px;
    height: 2317px;
    overflow: hidden;
    background: var(--stage);
  }
  .cover {
    position: absolute;
    left: 100px;
    top: 408px;
    width: 1000px;
    height: 1500px;
    overflow: hidden;
    background: radial-gradient(ellipse 70% 40% at 50% 95%, var(--cover-light) 0%, var(--cover) 70%);
    box-shadow: 0 30px 60px rgba(160, 40, 90, 0.25);
  }
  .heart-frame {
    position: absolute;
    left: 0; top: 0;
    width: 1000px; height: 1500px;
  }
  .dot { position: absolute; border-radius: 50%; background: var(--white); }
  .icon {
    position: absolute;
    background: var(--icon-fill);
    border: 6px solid var(--white);
    border-radius: 28px;
  }
  .icon--mask { left: 40px; top: 121px; width: 284px; height: 172px; border-radius: 90px; transform: rotate(-14deg); }
  .icon--heel { left: 380px; top: 224px; width: 185px; height: 224px; }
  .icon--condom { left: 729px; top: 121px; width: 216px; height: 215px; }
  .icon--plug { left: 74px; top: 1233px; width: 138px; height: 198px; border-radius: 60px 60px 20px 20px; }
  .icon--lips { left: 341px; top: 1172px; width: 302px; height: 173px; border-radius: 50%; border-color: var(--white); }
  .icon--tv { left: 738px; top: 1198px; width: 190px; height: 198px; }

  .title-pre {
    position: absolute;
    left: 70px; top: 470px;
    font-family: "Titan One", sans-serif;
    font-size: 40px;
    color: var(--white);
    text-transform: uppercase;
    letter-spacing: 1px;
    transform: rotate(-34deg);
    transform-origin: left center;
    text-shadow: 3px 3px 0 var(--title-shadow);
    white-space: nowrap;
  }
  .title-main {
    position: absolute;
    left: 0; top: 420px;
    width: 1000px;
    text-align: center;
    font-family: "Titan One", sans-serif;
    font-size: 310px;
    line-height: 1;
    color: var(--white);
    transform: rotate(-6deg);
    text-shadow: 10px 12px 0 var(--title-shadow);
    letter-spacing: -4px;
  }
  .title-sub {
    position: absolute;
    left: 0; top: 780px;
    width: 1000px;
    text-align: center;
    font-family: "Titan One", sans-serif;
    font-size: 104px;
    line-height: 1;
    color: var(--white);
    transform: rotate(-7deg);
    text-shadow: 7px 8px 0 var(--title-shadow);
    letter-spacing: -2px;
  }
  .badge {
    position: absolute;
    left: 333px; top: 936px;
    width: 353px; height: 90px;
    background: var(--badge);
    transform: rotate(-3deg);
    font-family: "Bebas Neue", sans-serif;
    font-size: 82px;
    line-height: 96px;
    text-align: center;
    color: var(--badge-text);
  }
  .subtitle {
    position: absolute;
    left: 0; top: 1040px;
    width: 1000px;
    text-align: center;
    font-family: "Bebas Neue", sans-serif;
    font-size: 56px;
    line-height: 58px;
    letter-spacing: 2px;
    color: var(--white);
    text-transform: uppercase;
  }
</style>
</head>
<body>
  <main class="cover">
    <svg class="heart-frame" viewBox="0 0 1000 1500" aria-hidden="true">
      <path d="M500 330 C 430 180, 200 110, 90 260 C -20 420, 60 640, 250 780 L 500 931 L 750 780 C 940 640, 1020 420, 910 260 C 800 110, 570 180, 500 330 Z"
            fill="none" stroke="var(--heart-line)" stroke-width="44" stroke-linejoin="round"/>
    </svg>

    <span class="dot" style="left:392px;top:40px;width:30px;height:30px"></span>
    <span class="dot" style="left:515px;top:95px;width:38px;height:38px"></span>
    <span class="dot" style="left:738px;top:36px;width:38px;height:38px"></span>
    <span class="dot" style="left:620px;top:180px;width:24px;height:24px"></span>
    <span class="dot" style="left:880px;top:370px;width:30px;height:30px"></span>
    <span class="dot" style="left:895px;top:490px;width:16px;height:16px"></span>
    <span class="dot" style="left:252px;top:1262px;width:18px;height:18px"></span>
    <span class="dot" style="left:280px;top:1348px;width:38px;height:38px"></span>
    <span class="dot" style="left:690px;top:1152px;width:24px;height:24px"></span>
    <span class="dot" style="left:700px;top:1235px;width:12px;height:12px"></span>

    <div class="icon icon--mask" role="img" aria-label="Icon: Augenmaske"></div>
    <div class="icon icon--heel" role="img" aria-label="Icon: High Heel"></div>
    <div class="icon icon--condom" role="img" aria-label="Icon: Kondompackungen"></div>

    <p class="title-pre">Der dicke</p>
    <h1 class="title-main">LUST</h1>
    <p class="title-sub">WUNSCHZETTEL</p>
    <p class="badge">150 Orte</p>
    <p class="subtitle">+10 eigene Orte für mehr<br>Nervenkitzel und Erlebnisse</p>

    <div class="icon icon--plug" role="img" aria-label="Icon: Toy"></div>
    <div class="icon icon--lips" role="img" aria-label="Icon: Kussmund"></div>
    <div class="icon icon--tv" role="img" aria-label="Icon: Fernseher mit XXX"></div>
  </main>
</body>
</html>
```